Lavoie Roofing

Want a professional looking business card

Industry/Entity Type

Business

Contact Information for Business Card

Mark Lavoie ( Owner) mark@lavoieroofing.example, www.lavoieroofing.example, Adress: 4712 County road 31 Maplecrest,NB E4X 2M4

```html
<!DOCTYPE html>
<html lang="en">
<head>
<meta charset="utf-8">
<title>Lavoie Roofing – Business Card</title>
<link rel="stylesheet" href="https://fonts.googleapis.com/css2?family=Questrial&display=swap">
<style>
  :root {
    --brand-blue: #1b4486;
    --card-white: #ffffff;
    --accent-grey: #8a8c90;
    --text-dark: #2c2c2c;
    --text-muted: #6b6b6b;
    --divider: #c9c9c9;
    --backdrop: #e6e7e9;
  }
  * { margin: 0; padding: 0; box-sizing: border-box; }
  html, body {
    width: 1200px; height: 675px; overflow: hidden;
    background: var(--backdrop);
    font-family: "Questrial", sans-serif;
  }
  .stage {
    position: relative; width: 1200px; height: 675px;
    display: flex; align-items: center; justify-content: center; gap: 50px;
  }
  .card {
    position: relative; width: 525px; height: 300px;
    box-shadow: 0 6px 18px rgba(0,0,0,0.18);
    overflow: hidden;
  }
  /* Front */
  .card-front {
    background: var(--brand-blue); color: var(--card-white);
    display: flex; flex-direction: column; align-items: center;
  }
  .front-brand {
    margin-top: 112px;
    display: flex; align-items: center; gap: 12px;
    font-size: 34px; letter-spacing: 3px; text-transform: uppercase;
    color: var(--card-white);
  }
  .brand-square {
    width: 16px; height: 16px; background: var(--card-white);
  }
  .front-web {
    position: absolute; bottom: 20px; left: 0; right: 0; text-align: center;
    font-size: 11px; letter-spacing: 3.2px;
  }
  /* Back */
  .card-back { background: var(--card-white); }
  .back-brand {
    position: absolute; left: 44px; top: 118px; width: 200px;
    display: flex; align-items: center; justify-content: center; gap: 8px;
    font-size: 19px; letter-spacing: 1.5px; text-transform: uppercase;
    color: var(--brand-blue);
  }
  .back-brand .brand-square { width: 10px; height: 10px; background: var(--brand-blue); }
  .back-divider {
    position: absolute; left: 258px; top: 66px; width: 1px; height: 114px;
    background: var(--divider);
  }
  .contact {
    position: absolute; left: 276px; top: 62px; color: var(--text-dark);
  }
  .contact-name { font-size: 21px; color: var(--brand-blue); letter-spacing: -0.3px; }
  .contact-role { font-size: 12px; color: var(--text-muted); margin-top: 2px; margin-left: 4px; }
  .contact-address { font-size: 10px; line-height: 15px; margin-top: 10px; margin-left: 4px; }
  .contact-line {
    display: flex; align-items: center; gap: 7px;
    font-size: 10px; margin-top: 5px; margin-left: 10px;
  }
  .contact-line svg { width: 9px; height: 9px; flex: none; }
  .bottom-bar {
    position: absolute; left: 0; bottom: 0; width: 432px; height: 8px;
    background: var(--brand-blue);
  }
  .bottom-accent {
    position: absolute; right: 0; bottom: 0; width: 98px; height: 20px;
    background: var(--accent-grey);
    clip-path: polygon(12px 0, 100% 0, 100% 100%, 0 100%);
  }
</style>
</head>
<body>
<main class="stage">
  <section class="card card-front">
    <div class="front-brand"><span class="brand-square"></span>Lavoie Roofing</div>
    <p class="front-web">www.lavoieroofing.example</p>
  </section>

  <section class="card card-back">
    <div class="back-brand"><span class="brand-square"></span>Lavoie Roofing</div>
    <div class="back-divider"></div>
    <div class="contact">
      <p class="contact-name">Mark Lavoie</p>
      <p class="contact-role">Owner</p>
      <p class="contact-address">4712 County road 31 Maplecrest,<br>NB E4X 2M4</p>
      <p class="contact-line">
        <svg viewBox="0 0 10 10" aria-hidden="true"><rect x="0.5" y="2" width="9" height="6.5" fill="none" stroke="#2c2c2c" stroke-width="1"/><path d="M0.5 2 L5 5.5 L9.5 2" fill="none" stroke="#2c2c2c" stroke-width="1"/></svg>
        mark@lavoieroofing.example
      </p>
      <p class="contact-line">
        <svg viewBox="0 0 10 10" aria-hidden="true"><circle cx="5" cy="5" r="4.3" fill="none" stroke="#2c2c2c" stroke-width="1"/><ellipse cx="5" cy="5" rx="1.8" ry="4.3" fill="none" stroke="#2c2c2c" stroke-width="0.8"/><line x1="0.7" y1="5" x2="9.3" y2="5" stroke="#2c2c2c" stroke-width="0.8"/></svg>
        www.lavoieroofing.example
      </p>
    </div>
    <div class="bottom-bar"></div>
    <div class="bottom-accent"></div>
  </section>
</main>
</body>
</html>
```